Business card design for new, innovative company - BluePlinth

We are a new company looking for a business card design that is fun, different and quirky. Must use corporate colour green - CMYK C:55, M:0, Y:100, K:0, and corporate colour grey - C:0, M:0, Y: 0, K:70.

We have developed the first real time data application, in which people are able to profile the data of their existing customers in order to pull out more good fit clients to direct their marketing activities at.

Industry/Entity Type

Marketing

Requirements
Must have
• Logo, name, title, telephone number, fax number, email, website, address

```html
<!DOCTYPE html>
<html lang="en">
<head>
<meta charset="utf-8">
<title>BluePlinth Business Card</title>
<link href="https://fonts.googleapis.com/css2?family=PT+Sans+Narrow:wght@400;700&family=Source+Sans+3:wght@400;600&display=swap" rel="stylesheet">
<style>
  :root {
    --brand-grey: #6d6e70;
    --brand-green: #7dc142;
    --frame-orange: #c3652f;
    --label-grey: #4e4f51;
    --white: #ffffff;
    --page: #e9e9e7;
  }
  * { margin: 0; padding: 0; box-sizing: border-box; }
  html, body { width: 1200px; height: 900px; overflow: hidden; }
  body { background: var(--page); position: relative; font-family: "PT Sans Narrow", sans-serif; }

  .card {
    position: absolute;
    top: 305px;
    width: 520px;
    height: 290px;
    background: var(--brand-grey);
    border-radius: 12px;
    box-shadow: 0 6px 18px rgba(0,0,0,0.22);
    overflow: hidden;
  }
  .card--front { left: 70px; }
  .card--back { left: 610px; }

  .card__frame {
    position: absolute;
    inset: 16px;
    border: 1px solid var(--frame-orange);
    border-radius: 14px;
    z-index: 3;
    pointer-events: none;
  }

  .wordmark {
    font-family: "Source Sans 3", sans-serif;
    font-weight: 600;
    color: var(--white);
    letter-spacing: -0.5px;
  }
  .card--front .wordmark {
    position: absolute;
    top: 50px;
    left: 0; right: 0;
    text-align: center;
    font-size: 28px;
  }

  .green-band { position: absolute; left: 0; top: 118px; width: 520px; height: 130px; z-index: 1; }

  .holder-name {
    position: absolute;
    left: 36px; top: 146px;
    font-size: 17px; font-weight: 700;
    color: var(--white);
    letter-spacing: 0.3px;
    z-index: 2;
  }
  .address {
    position: absolute;
    left: 36px; top: 184px;
    font-size: 12px; font-weight: 700;
    color: var(--white);
    line-height: 1.2;
    display: flex; gap: 10px;
    z-index: 2;
  }
  .label { color: var(--label-grey); font-weight: 700; white-space: nowrap; }

  .contacts {
    position: absolute;
    right: 30px; top: 143px;
    list-style: none;
    text-align: right;
    z-index: 2;
  }
  .contacts li {
    font-size: 12.5px; font-weight: 700;
    color: var(--white);
    line-height: 1;
  }
  .contacts li + li { margin-top: 7px; }
  .contacts .contacts__email { margin-top: 12px; }
  .contacts .contacts__web { margin-top: 14px; }
  .contacts .label { margin-right: 8px; }

  .back-name {
    position: absolute;
    top: 50px; left: 0; right: 0;
    text-align: center;
    font-size: 9px;
    color: var(--white);
    letter-spacing: 0.3px;
  }
  .back-badge {
    position: absolute;
    left: 170px; top: 106px;
    width: 180px; height: 62px;
  }
  .back-badge .wordmark {
    position: absolute;
    inset: 0;
    display: flex; align-items: center; justify-content: center;
    font-size: 27px;
  }
</style>
</head>
<body>

<section class="card card--front" aria-label="Business card front">
  <div class="card__frame"></div>
  <div class="wordmark">BluePlinth</div>

  <svg class="green-band" viewBox="0 0 520 130" aria-hidden="true">
    <path fill="var(--brand-green)" d="M0 14 L18 10 L34 13 L52 8 L70 12 L88 9 L104 13 L122 7 L140 11 L158 8 L176 12 L194 6 L212 10 L230 7 L248 11 L266 6 L284 9 L302 5 L320 9 L338 4 L356 8 L374 3 L392 7 L410 2 L428 6 L446 1 L464 5 L482 0 L500 4 L520 1
      L520 118 L502 121 L484 117 L466 122 L448 118 L430 123 L412 119 L394 124 L376 120 L358 125 L340 121 L322 126 L304 122 L286 127 L268 122 L250 127 L232 123 L214 128 L196 123 L178 127 L160 122 L142 126 L124 121 L106 125 L88 120 L70 124 L52 119 L34 123 L16 118 L0 122 Z"/>
  </svg>

  <div class="holder-name">CARLA DENTON</div>
  <div class="address">
    <span class="label">{ A }</span>
    <span>22a Mere Lane, Ely,<br>Cambridgeshire, CB7 4QR</span>
  </div>

  <ul class="contacts">
    <li><span class="label">{ M }</span>07700900417</li>
    <li><span class="label">{ T }</span>01632 960284</li>
    <li class="contacts__email"><span class="label">{ E }</span>carla.denton@fenwaysupply.com</li>
    <li class="contacts__web"><span class="label">{ W }</span>www.blueplinth.com</li>
  </ul>
</section>

<section class="card card--back" aria-label="Business card back">
  <div class="card__frame"></div>
  <div class="back-name">CARLA DENTON</div>
  <div class="back-badge">
    <svg viewBox="0 0 180 62" width="180" height="62" aria-hidden="true">
      <path fill="var(--brand-green)" d="M4 3 L30 1 L60 4 L92 0 L124 3 L152 1 L177 4 L175 20 L179 36 L176 50 L178 60 L150 58 L120 62 L90 59 L60 61 L30 58 L3 61 L5 46 L1 32 L4 18 Z"/>
    </svg>
    <div class="wordmark">BluePlinth</div>
  </div>
</section>

</body>
</html>
```